Business Card

I would like a business card with a picture of my husband and I that is unique and professional.

Industry/Entity Type

Business

Font styles to use
Serif

```html
<!DOCTYPE html>
<html lang="en">
<head>
<meta charset="utf-8">
<title>Halden Leadership Group – Business Card</title>
<link rel="stylesheet" href="https://fonts.googleapis.com/css2?family=Cinzel:wght@400;600&family=Josefin+Sans:wght@300;400&display=swap">
<style>
  :root {
    --backdrop: #d9d9d9;
    --card-black: #141414;
    --card-black-edge: #262626;
    --card-white: #ffffff;
    --gold: #d8a53a;
    --gold-light: #f0c866;
    --ink: #1c1c1c;
    --ink-soft: #3a3a3a;
    --photo-light: #e6e4e2;
    --photo-mid: #9c9a98;
    --photo-dark: #5d5553;
  }
  * { box-sizing: border-box; margin: 0; padding: 0; }
  html, body { width: 1200px; height: 900px; overflow: hidden; }
  body {
    background: var(--backdrop);
    position: relative;
    font-family: "Josefin Sans", Arial, sans-serif;
  }
  .card {
    position: absolute;
    left: 260px;
    width: 680px;
    height: 388px;
    border-radius: 4px;
    overflow: hidden;
    box-shadow: 0 8px 24px rgba(0,0,0,0.25);
  }
  /* Front */
  .card-front {
    top: 46px;
    background: linear-gradient(160deg, var(--card-black-edge), var(--card-black) 60%);
  }
  .brand-mark {
    position: absolute;
    top: 92px; left: 0; right: 0;
    display: flex; align-items: center; justify-content: center; gap: 16px;
  }
  .brand-mark .dot {
    width: 22px; height: 22px; border-radius: 50%;
    background: var(--gold);
  }
  .brand-mark .name {
    font-family: "Cinzel", Georgia, serif;
    font-weight: 600;
    font-size: 64px;
    color: var(--gold);
    letter-spacing: 2px;
  }
  .company-line {
    position: absolute;
    left: 0; right: 0;
    text-align: center;
  }
  .company-line .company {
    font-family: "Cinzel", Georgia, serif;
    font-weight: 600;
    color: var(--gold);
    letter-spacing: 1px;
  }
  .card-front .company-line { top: 262px; }
  .card-front .company { font-size: 28px; }
  .rule-svg { display: block; margin: 6px auto 0; }

  /* Back */
  .card-back {
    top: 466px;
    background: var(--card-white);
  }
  .portrait {
    position: absolute;
    right: 0; top: 0;
    width: 330px; height: 100%;
    background:
      radial-gradient(ellipse at 55% 30%, var(--photo-dark) 0 18%, transparent 40%),
      radial-gradient(ellipse at 60% 75%, var(--photo-mid) 0 30%, transparent 60%),
      linear-gradient(90deg, var(--card-white), var(--photo-light) 30%, var(--photo-light));
  }
  .details {
    position: absolute;
    left: 30px; top: 30px;
    width: 340px;
  }
  .person-name {
    font-size: 30px;
    font-weight: 300;
    color: var(--gold);
    letter-spacing: 2px;
    text-transform: uppercase;
  }
  .person-title {
    font-size: 13px;
    color: var(--ink);
    letter-spacing: 1px;
    text-transform: uppercase;
    margin-top: 2px;
  }
  .dotted { border-top: 2px dotted var(--ink-soft); margin: 8px 0; }
  .contact-list { list-style: none; }
  .contact-list li {
    display: flex; align-items: center; gap: 10px;
    font-size: 18px; color: var(--ink); line-height: 28px;
  }
  .contact-list svg { flex: none; }
  .address { font-size: 18px; color: var(--ink); margin-top: 4px; }
  .card-back .company-line {
    top: 300px; left: 30px; right: auto; width: 340px;
  }
  .card-back .company { font-size: 20px; }
</style>
</head>
<body>

  <section class="card card-front" aria-label="Card front">
    <div class="brand-mark">
      <span class="dot"></span>
      <span class="name">Halden</span>
    </div>
    <div class="company-line">
      <div class="company">Halden Leadership Group</div>
      <svg class="rule-svg" width="520" height="14" viewBox="0 0 520 14" aria-hidden="true">
        <line x1="0" y1="7" x2="520" y2="7" stroke="#d8a53a" stroke-width="2"/>
        <polygon points="260,2 265,7 260,12 255,7" fill="#d8a53a"/>
      </svg>
    </div>
  </section>

  <section class="card card-back" aria-label="Card back">
    <div class="portrait" role="img" aria-label="Portrait photo of the husband and wife"></div>

    <div class="details">
      <div class="person-name">Renata Halden</div>
      <div class="person-title">Professional Mentorship Strategist</div>
      <div class="dotted"></div>
      <ul class="contact-list">
        <li>
          <svg width="18" height="18" viewBox="0 0 24 24" aria-hidden="true"><path d="M6.6 10.8a15 15 0 0 0 6.6 6.6l2.2-2.2a1 1 0 0 1 1-.25 11.4 11.4 0 0 0 3.6.57 1 1 0 0 1 1 1V20a1 1 0 0 1-1 1A17 17 0 0 1 3 4a1 1 0 0 1 1-1h3.5a1 1 0 0 1 1 1 11.4 11.4 0 0 0 .57 3.6 1 1 0 0 1-.25 1z" fill="#1c1c1c"/></svg>
          <span>: 555-014-2290 Direct</span>
        </li>
        <li>
          <svg width="18" height="18" viewBox="0 0 24 24" aria-hidden="true"><rect x="2" y="5" width="20" height="14" fill="none" stroke="#1c1c1c" stroke-width="2"/><polyline points="2,5 12,13 22,5" fill="none" stroke="#1c1c1c" stroke-width="2"/></svg>
          <span>: RenataHalden@example.com</span>
        </li>
        <li>
          <svg width="18" height="18" viewBox="0 0 24 24" aria-hidden="true"><circle cx="12" cy="12" r="10" fill="none" stroke="#1c1c1c" stroke-width="2"/><ellipse cx="12" cy="12" rx="4.5" ry="10" fill="none" stroke="#1c1c1c" stroke-width="1.5"/><line x1="2" y1="12" x2="22" y2="12" stroke="#1c1c1c" stroke-width="1.5"/></svg>
          <span>: www.yoursite.com</span>
        </li>
      </ul>
      <div class="address">Your address go here</div>
      <div class="dotted"></div>
    </div>

    <div class="company-line">
      <div class="company">Halden Leadership Group</div>
      <svg class="rule-svg" width="340" height="12" viewBox="0 0 340 12" aria-hidden="true">
        <line x1="0" y1="6" x2="340" y2="6" stroke="#d8a53a" stroke-width="2"/>
        <polygon points="170,2 174,6 170,10 166,6" fill="#d8a53a"/>
      </svg>
    </div>
  </section>

</body>
</html>
```